Pellmark Ridgeway LLC stationery, business card and web page design.

i need a full set of stationery designed using the name "Pellmark Ridgeway LLC" with a tag line "construction consulting services". using the uploaded monkey icon as the logo.

i like the colors orange, green and black in general but im not limited to that. the company offers consulting services to various types of construction businesses.

i travel around the country in a 4x4 camper offering consulting services and technical training short term and long to various types of construction companies.

Construction Company

Peter Lund
p.lund@pellmarkridgeway.example
2748 Fenwick Rd
Maple Glen, NY 10943
555 014 3627

list these services on the card.

Business Consulting
Capital Investments
Marketing Implementations
Technical Training

1 page

Designer to choose colors to be used in the design.

• company info and use of the monkey icon i provided.
• a fun but professional design
• the color red

```html
<!DOCTYPE html>
<html lang="en">
<head>
<meta charset="utf-8">
<title>Pellmark Ridgeway LLC – Business Card</title>
<link rel="stylesheet" href="https://fonts.googleapis.com/css2?family=Cinzel:wght@400;600;700&family=Roboto:wght@400;500&display=swap">
<style>
  :root {
    --backdrop: #e6e3df;
    --card-white: #f7f7f6;
    --brand-orange: #fa5e1f;
    --ink: #161616;
    --text-grey: #555555;
    --rule-grey: #9a9a9a;
    --white: #ffffff;
  }
  * { margin: 0; padding: 0; box-sizing: border-box; }
  html, body { width: 1200px; height: 960px; overflow: hidden; }
  body { position: relative; background: var(--backdrop); font-family: "Roboto", Arial, sans-serif; }

  .card {
    position: absolute;
    left: 300px;
    width: 598px;
    height: 341px;
    border-radius: 18px;
    overflow: hidden;
    box-shadow: 0 3px 8px rgba(0,0,0,0.25);
  }
  .card--front { top: 137px; background: var(--card-white); }
  .card--back { top: 489px; background: var(--brand-orange); }

  .brand-mark {
    position: absolute;
    border-radius: 50%;
    background: var(--ink);
  }
  .card--front .brand-mark { left: 396px; top: 18px; width: 112px; height: 112px; }
  .card--back .brand-mark { left: 214px; top: 56px; width: 170px; height: 170px; }

  .brand-name {
    position: absolute;
    font-family: "Cinzel", "Times New Roman", serif;
    font-weight: 600;
    white-space: nowrap;
    text-align: center;
  }
  .brand-tagline {
    position: absolute;
    font-family: "Cinzel", "Times New Roman", serif;
    font-weight: 600;
    color: var(--ink);
    white-space: nowrap;
    text-align: center;
  }
  .card--front .brand-name { left: 320px; width: 264px; top: 152px; font-size: 17px; color: var(--brand-orange); }
  .card--front .brand-tagline { left: 320px; width: 264px; top: 175px; font-size: 9px; }
  .card--back .brand-name { left: 0; width: 598px; top: 240px; font-size: 24px; color: var(--ink); }
  .card--back .brand-tagline { left: 0; width: 598px; top: 272px; font-size: 13px; letter-spacing: 0.2px; }

  .holder-name {
    position: absolute; left: 27px; top: 159px;
    font-family: "Cinzel", "Times New Roman", serif;
    font-size: 24px; font-weight: 400; color: var(--brand-orange);
  }
  .holder-title {
    position: absolute; left: 27px; top: 186px;
    font-family: "Cinzel", "Times New Roman", serif;
    font-size: 15px; font-weight: 700; color: var(--ink);
  }
  .divider {
    position: absolute; left: 27px; top: 214px; width: 539px; height: 1px;
    background: var(--rule-grey);
  }

  .contact-list { position: absolute; left: 28px; top: 228px; list-style: none; }
  .contact-list li {
    display: flex; align-items: center; height: 19px;
    font-size: 14px; color: var(--text-grey);
  }
  .contact-list svg { width: 14px; height: 14px; margin-right: 9px; fill: var(--brand-orange); }

  .office-address {
    position: absolute; right: 32px; top: 249px;
    text-align: right; font-style: normal;
    font-size: 14px; line-height: 18px; color: var(--text-grey);
  }
  .office-address strong { font-weight: 500; color: #444; }

  .footer-band { position: absolute; left: 0; top: 0; width: 598px; height: 341px; }
  .website {
    position: absolute; left: 358px; top: 320px;
    font-size: 14px; letter-spacing: 1.2px; color: var(--white);
  }
</style>
</head>
<body>

  <section class="card card--front" aria-label="Business card front">
    <svg class="footer-band" viewBox="0 0 598 341" aria-hidden="true">
      <path d="M0 320 L342 320 C330 320 328 332 316 332 L0 332 Z" fill="var(--ink)"/>
      <path d="M324 341 C340 341 342 316 360 316 L598 316 L598 341 Z" fill="var(--brand-orange)"/>
    </svg>

    <div class="brand-mark" aria-hidden="true"></div>
    <div class="brand-name">PELLMARK RIDGEWAY LLC</div>
    <div class="brand-tagline">CONSTRUCTION CONSULTING SERVICES</div>

    <div class="holder-name">PETER LUND</div>
    <div class="holder-title">CEO/FOUNDER</div>
    <div class="divider"></div>

    <ul class="contact-list">
      <li>
        <svg viewBox="0 0 16 16" aria-hidden="true"><path d="M3.2 1.2l2.4 2.6-1.2 1.8c.9 2 2.6 3.7 4.6 4.6l1.8-1.2 2.6 2.4-1.4 2.6C6.6 13.8 2.2 9.4 1.2 3.2z"/></svg>
        555 014 3627
      </li>
      <li>
        <svg viewBox="0 0 16 16" aria-hidden="true"><path d="M4.5 1h7a1 1 0 0 1 1 1v12a1 1 0 0 1-1 1h-7a1 1 0 0 1-1-1V2a1 1 0 0 1 1-1zm.5 2v9h6V3zm3 10a.7.7 0 1 0 0 1.4.7.7 0 0 0 0-1.4z"/></svg>
        555 014 7781
      </li>
      <li>
        <svg viewBox="0 0 16 16" aria-hidden="true"><path d="M4 1h8v4H4zM1.5 6h13a1 1 0 0 1 1 1v5h-3v3h-9v-3h-3V7a1 1 0 0 1 1-1zm3.5 5v2.5h6V11z"/></svg>
        555 014 2209
      </li>
      <li>
        <svg viewBox="0 0 16 16" aria-hidden="true"><path d="M1 3.5h14v9H1zm1.4 1.2L8 9l5.6-4.3z" fill-rule="evenodd"/></svg>
        p.lund@pellmarkridgeway.example
      </li>
    </ul>

    <address class="office-address">
      <strong>Pellmark Ridgeway LLC</strong><br>
      2748 Fenwick Rd<br>
      Maple Glen, NY 10943
    </address>

    <div class="website">www.pellmarkridgeway.example</div>
  </section>

  <section class="card card--back" aria-label="Business card back">
    <div class="brand-mark" aria-hidden="true"></div>
    <div class="brand-name">PELLMARK RIDGEWAY LLC</div>
    <div class="brand-tagline">CONSTRUCTION CONSULTING SERVICES</div>
  </section>

</body>
</html>
```